Manuka honey wholesales and exports

We need business cards for our honey distribution company based in New Zealand. We supply shops locally and export Manuka honey around the world.
We deal with a very high quality and 100% natural product that can be used for medical, general health as well as food. We are looking business cards that show our honey products are of a high quality with a modern look.

Target Market(s)

Health and medical retailers and importers

Industry/Entity Type

Wholesale

Contact Information for Business Card

Tevin Apiary NZ Limited

www.tevinapiarynz.example

Derek Fawley

M +64 219036482

E tevinapiarynz@mailbox.example

PO Box 58-214
Takapuna
North Shore
Auckland
New Zealand

Font styles to use
Serif

Requirements
Must have
• (Tevin Apiary NZ Limited) with some artwork on one side and all details on the other side.
Nice to have
• I have seen a very simple card with large yellow and black stripes on one side with a company name.. looked clean and simple so something similar or just let the creative beast inside you take over and we will see what you can come up with.

```html
<!DOCTYPE html>
<html lang="en">
<head>
<meta charset="utf-8">
<title>Tevin Apiary business card</title>
<link rel="stylesheet" href="https://fonts.googleapis.com/css2?family=Asap:wght@400;600;700&display=swap">
<style>
  :root {
    --honey: #f5b236;
    --honey-deep: #eaa52e;
    --brown: #421a0b;
    --backdrop: #ebebeb;
  }
  html, body {
    margin: 0;
    padding: 0;
    width: 1200px;
    height: 576px;
    overflow: hidden;
    background: var(--backdrop);
    font-family: "Asap", Arial, sans-serif;
  }
  .canvas {
    position: relative;
    width: 1200px;
    height: 576px;
  }
  .card {
    position: absolute;
    top: 138px;
    width: 484px;
    height: 294px;
    border-radius: 13px;
    background: linear-gradient(180deg, var(--honey) 0%, var(--honey) 60%, var(--honey-deep) 100%);
    overflow: hidden;
    color: var(--brown);
  }
  .card--front { left: 82px; }
  .card--back { left: 602px; width: 480px; }

  .brand {
    position: absolute;
    display: flex;
    flex-direction: column;
    align-items: center;
  }
  .brand__mark {
    width: 54px;
    height: 54px;
    background: var(--brown);
    border-radius: 4px;
  }
  .brand__name {
    margin-top: 10px;
    font-weight: 600;
    font-size: 30px;
    line-height: 1;
    letter-spacing: -0.3px;
    white-space: nowrap;
  }
  .card--front .brand { right: 21px; top: 28px; }
  .card--back .brand { left: 50%; top: 83px; transform: translateX(-50%); }

  .holder {
    position: absolute;
    left: 20px;
    right: 21px;
    top: 160px;
    display: flex;
    align-items: flex-end;
    gap: 12px;
  }
  .holder__name {
    font-weight: 700;
    font-size: 22px;
    line-height: 1;
    letter-spacing: -0.3px;
    white-space: nowrap;
  }
  .holder__rule {
    flex: 1;
    height: 1px;
    background: var(--brown);
    margin-bottom: 1px;
  }

  .contacts {
    position: absolute;
    left: 21px;
    top: 205px;
    margin: 0;
    padding: 0;
    list-style: none;
    font-size: 12px;
    line-height: 16.5px;
  }
  .contacts li {
    display: flex;
    align-items: center;
    gap: 10px;
  }
  .contacts svg { width: 11px; height: 11px; flex: none; }

  .address {
    position: absolute;
    right: 21px;
    top: 215px;
    margin: 0;
    text-align: right;
    font-style: normal;
    font-size: 12px;
    line-height: 16.5px;
  }

  .band {
    position: absolute;
    left: 0;
    bottom: 0;
    width: 484px;
    height: 28px;
  }
</style>
</head>
<body>
<main class="canvas">
  <section class="card card--front" aria-label="Card front with contact details">
    <div class="brand">
      <div class="brand__mark"></div>
      <div class="brand__name">Tevin Apiary</div>
    </div>

    <div class="holder">
      <span class="holder__name">Derek Fawley</span>
      <span class="holder__rule"></span>
    </div>

    <ul class="contacts">
      <li>
        <svg viewBox="0 0 12 12" aria-hidden="true"><rect x="3" y="0.5" width="6" height="11" rx="1" fill="none" stroke="#421a0b" stroke-width="1.2"/><rect x="4.2" y="2" width="3.6" height="6.5" fill="#421a0b"/></svg>
        <span>+64 219036482</span>
      </li>
      <li>
        <svg viewBox="0 0 12 12" aria-hidden="true"><rect x="0.5" y="2.5" width="11" height="7" fill="#421a0b"/><path d="M0.5 2.5 L6 7 L11.5 2.5" fill="none" stroke="#f5b236" stroke-width="1"/></svg>
        <span>tevinapiarynz@mailbox.example</span>
      </li>
      <li>
        <svg viewBox="0 0 12 12" aria-hidden="true"><circle cx="6" cy="6" r="5.2" fill="#421a0b"/><path d="M0.8 6 H11.2 M6 0.8 C3.5 3.5 3.5 8.5 6 11.2 M6 0.8 C8.5 3.5 8.5 8.5 6 11.2" fill="none" stroke="#f5b236" stroke-width="0.8"/></svg>
        <span>www.tevinapiarynz.example</span>
      </li>
    </ul>

    <address class="address">PO Box 58-214 Kerewai North<br>Shore Tamaroa NZ</address>

    <svg class="band" viewBox="0 0 484 28" preserveAspectRatio="none" aria-hidden="true">
      <polygon points="0,13 263,13 250,28 0,28" fill="#421a0b"/>
      <polygon points="282,0 484,0 484,28 258,28" fill="#421a0b"/>
      <line x1="278" y1="0" x2="253" y2="28" stroke="#f5b236" stroke-width="1.5"/>
    </svg>
  </section>

  <section class="card card--back" aria-label="Card back with company name">
    <div class="brand">
      <div class="brand__mark"></div>
      <div class="brand__name">Tevin Apiary</div>
    </div>
  </section>
</main>
</body>
</html>
```